Happy Birthday Postcard for law firm for existing clients

Need a postcard that will go out to our current clients on their birthdays. Prefer to have our logo incorporated as part of the design so it reminds them about our business. The back needs to say "Happy Birthday from the team at Brantley Law Firm."

We are a law firm that services local clients. Needs to be mailed so the backside right half needs to be left blank except the return address (in NEEDS below) so it can be mailed with a mailing label.

Target Market(s)

existing customers, varying age range and demographic profile

Industry/Entity Type

Legal

Font styles to use
Sans Serif
Script

Colors

Designer to choose colors to be used in the design.

Requirements
Must have
• Our logo preferrably on the front (can be modified or added to so it fits a birthday message. And needs to be mailed so the back right side needs to be left open for address labels. The firms return address is
• Brantley Law Firm
• 7150 W Copperfield Ave
• Springfield, MO 65817
• Needs to have the text included in the project description on the back, or some close iteration of it if space is limited.
Nice to have
• Some illustration or graphic on the front with the logo that shows it is a birthday postcard

```html
<!DOCTYPE html>
<html lang="en">
<head>
<meta charset="utf-8">
<title>Brantley Law Firm – Birthday Postcard</title>
<link rel="stylesheet" href="https://fonts.googleapis.com/css2?family=Kaushan+Script&family=Lato:wght@400&display=swap">
<style>
  :root {
    --navy: #32547c;
    --navy-deep: #2b4a70;
    --confetti-sky: #3fb4ea;
    --confetti-blue: #2a7fd1;
    --confetti-pink: #e2578f;
    --plate-light: #ffffff;
    --plate-edge: #d9dbe0;
    --lettering: #e4eeff;
    --lettering-shade: #1f5aa8;
    --white: #ffffff;
  }
  html, body {
    margin: 0;
    padding: 0;
    overflow: hidden;
    background: var(--navy);
  }
  .postcard {
    position: relative;
    width: 930px;
    height: 1200px;
    background: var(--navy);
    overflow: hidden;
  }
  .confetti-burst {
    position: absolute;
    left: 88px;
    top: 221px;
    width: 754px;
    height: 754px;
  }
  .greeting-plate {
    position: absolute;
    left: 266px;
    top: 399px;
    width: 398px;
    height: 398px;
    border-radius: 50%;
    background: radial-gradient(circle at 50% 45%, var(--plate-light) 55%, #eef0f3 80%, var(--plate-edge) 100%);
    box-shadow: 0 0 0 3px rgba(255,255,255,0.85), 0 4px 14px rgba(0,0,0,0.25);
  }
  .greeting {
    position: absolute;
    left: 0;
    width: 930px;
    text-align: center;
    margin: 0;
    font-family: "Kaushan Script", cursive;
    font-weight: 400;
    color: var(--lettering);
    text-shadow: 2px 3px 0 var(--lettering-shade);
    line-height: 1;
  }
  .greeting--happy {
    top: 522px;
    font-size: 86px;
    transform: rotate(-6deg);
  }
  .greeting--birthday {
    top: 608px;
    font-size: 90px;
    transform: rotate(-6deg);
  }
  .ribbon {
    position: absolute;
    left: 404px;
    top: 704px;
    width: 122px;
    height: 50px;
  }
  .ribbon__text {
    font-family: "Lato", sans-serif;
    font-size: 21px;
    fill: var(--white);
  }
  .firm-name {
    position: absolute;
    left: 0;
    top: 1118px;
    width: 930px;
    text-align: center;
    margin: 0;
    font-family: "Lato", sans-serif;
    font-weight: 400;
    font-size: 34px;
    letter-spacing: 1px;
    color: var(--white);
  }
</style>
</head>
<body>
  <main class="postcard">
    <svg class="confetti-burst" viewBox="0 0 754 754" role="img" aria-label="Burst of blue, pink and white triangle confetti radiating around the greeting">
      <defs>
        <radialGradient id="confettiGlow" cx="50%" cy="50%" r="50%">
          <stop offset="0.5" stop-color="#4aa6e0" stop-opacity="0.9"/>
          <stop offset="0.62" stop-color="#6a8fd0" stop-opacity="0.75"/>
          <stop offset="0.78" stop-color="#c76ea3" stop-opacity="0.35"/>
          <stop offset="1" stop-color="#3a6aa0" stop-opacity="0"/>
        </radialGradient>
      </defs>
      <circle cx="377" cy="377" r="377" fill="url(#confettiGlow)"/>
    </svg>

    <div class="greeting-plate"></div>

    <p class="greeting greeting--happy">Happy</p>
    <p class="greeting greeting--birthday">Birthday</p>

    <svg class="ribbon" viewBox="0 0 122 50" aria-hidden="false">
      <path d="M4 6 Q61 30 118 6 L114 28 Q61 52 8 28 Z" fill="var(--navy)"/>
      <text class="ribbon__text" x="61" y="35" text-anchor="middle">TO YOU</text>
    </svg>

    <p class="firm-name">BRANTLEY LAW</p>
  </main>
</body>
</html>
```